Boutique Fitness Facility needs a new meal plan design that is as hot as our workouts!

We are about to host our 6 week Coral Blitz program and we need to have a great looking meal plan handout created that we can give to all of our participants.

I have attached an example of our current full meal plan, for a reference only.

As in the example I've provided, I'd like to have certain areas color coded such as the proteins being Blue, Fats -yellow, Carbs - orange and veggies- green.

These colors will corollate to the Breakfast - snack - lunch - snack - Dinner graph that I've provided and would like to have added to the new handout.

I would like our logo placed at the top and beneath the logo have the text "Coral Blitz Challenge"

The flyer should be of a summer influence in colors and design and
All text should be easy to read.

Thank you and I look forward to seeing your design!

```html
<!DOCTYPE html>
<html lang="en">
<head>
<meta charset="utf-8">
<title>Coral Blitz Challenge – Meal Plan</title>
<link rel="stylesheet" href="https://fonts.googleapis.com/css2?family=Archivo:ital,wght@1,900&family=Archivo+Black&family=Oswald:wght@500&family=Inter:wght@400;600&display=swap">
<style>
  :root {
    --sun: #f7d117;
    --ink: #0d0d0d;
    --protein: #05a8e8;
    --fats: #f7b500;
    --carbs: #f58a1f;
    --veg: #50b848;
    --snack: #ee3b2f;
    --card: #ffffff;
    --muted: #d9d9d9;
  }
  * { box-sizing: border-box; margin: 0; padding: 0; }
  html, body { width: 927px; height: 1200px; overflow: hidden; background: var(--ink); }
  .sheet { position: relative; width: 927px; height: 1200px; overflow: hidden; background: var(--ink); }

  .backdrop { position: absolute; inset: 0; }
  .hero-photo { position: absolute; left: 0; top: 380px; width: 927px; height: 820px;
    background: radial-gradient(ellipse at 50% 40%, #2a2a2a 0%, #141414 55%, #0b0b0b 100%); }

  .brand { position: absolute; top: 0; right: 0; width: 370px; height: 114px; }
  .brand-name { position: absolute; top: 14px; right: 40px; font-family: "Archivo Black", sans-serif;
    font-size: 50px; line-height: 1; color: var(--sun); letter-spacing: -1px; }
  .brand-tag { position: absolute; top: 85px; right: 70px; font-family: "Archivo Black", sans-serif;
    font-size: 9px; letter-spacing: 1.6px; color: var(--sun); }

  .title { position: absolute; left: 48px; top: 32px; font-family: "Archivo", sans-serif; font-weight: 900;
    font-style: italic; font-size: 67px; line-height: 62px; color: var(--ink); text-transform: uppercase; letter-spacing: -0.5px; }

  .food-groups { position: absolute; left: 28px; top: 243px; display: flex; gap: 12px; }
  .group { width: 209px; height: 329px; background: var(--card); border-radius: 8px; overflow: hidden; }
  .group-tab { height: 46px; width: 186px; padding: 14px 0 0 22px; font-family: "Archivo Black", sans-serif;
    font-size: 17.5px; color: var(--ink); clip-path: polygon(0 0, 100% 0, 88% 100%, 0 100%); letter-spacing: 0.3px; }
  .protein .group-tab { background: var(--protein); }
  .fats .group-tab { background: var(--fats); }
  .carbs .group-tab { background: var(--carbs); }
  .veg .group-tab { background: var(--veg); }
  .group ul { list-style: none; padding: 19px 10px 0 20px; font-family: "Oswald", sans-serif; font-weight: 500;
    font-size: 15px; line-height: 20.5px; color: var(--ink); text-transform: uppercase; }
  .group li { position: relative; padding-left: 18px; }
  .group li::before { content: ""; position: absolute; left: 0; top: 8px; width: 5px; height: 5px; border-radius: 50%; background: var(--ink); }

  .portion-note { position: absolute; left: 38px; top: 589px; width: 850px; height: 54px; border-radius: 27px;
    background: var(--sun); font-family: "Archivo Black", sans-serif; font-size: 16.3px; color: var(--ink);
    display: flex; align-items: center; justify-content: center; letter-spacing: 0.2px; }

  .meal-flow { position: absolute; left: 22px; top: 659px; width: 883px; height: 185px; border: 1.5px solid var(--sun); border-radius: 16px; }
  .meal { position: absolute; top: 16px; width: 152px; height: 152px; }
  .meal svg { display: block; }
  .snack { position: absolute; top: 63px; width: 110px; text-align: center; }
  .snack-arrow { display: block; margin: 0 auto; }
  .snack-note { margin-top: 4px; font-family: "Inter", sans-serif; font-size: 12.5px; line-height: 16px; color: #fff; }

  .fuel-title { position: absolute; top: 862px; left: 0; width: 927px; text-align: center; font-family: "Archivo Black", sans-serif;
    font-size: 33px; color: var(--sun); letter-spacing: 0.5px; }
  .fuel-intro { position: absolute; top: 920px; left: 60px; width: 807px; text-align: center; font-family: "Inter", sans-serif;
    font-weight: 600; font-size: 13.4px; line-height: 23px; color: #fff; }

  .tips { position: absolute; top: 989px; left: 0; width: 927px; height: 175px; }
  .tip { position: absolute; top: 0; }
  .tip h3 { font-family: "Archivo Black", sans-serif; font-size: 13.8px; line-height: 17px; color: var(--sun); font-weight: 400; text-transform: uppercase; }
  .tip p { margin-top: 7px; font-family: "Inter", sans-serif; font-size: 12.6px; line-height: 16.5px; color: var(--muted); }
  .tip-rule { position: absolute; top: 2px; width: 1.5px; height: 175px; background: var(--sun); }
</style>
</head>
<body>
<main class="sheet">
  <svg class="backdrop" width="927" height="1200" viewBox="0 0 927 1200" aria-hidden="true">
    <path fill="#f7d117" d="M0 0H927V430L900 428 880 436 850 430 800 437 760 432 720 440 690 436 680 448 620 450 580 446 560 456 520 452 480 460 440 456 400 410 360 414 320 408 280 418 240 412 200 420 160 415 120 422 80 418 40 426 0 420Z"/>
  </svg>
  <div class="hero-photo" role="img" aria-label="Dark photo of an athlete training with dumbbells"></div>
  <svg class="backdrop" width="927" height="1200" viewBox="0 0 927 1200" aria-hidden="true">
    <path fill="#f7d117" d="M0 0H927V330L0 330Z"/>
    <path fill="#f7d117" d="M0 330H927V430L900 428 880 436 850 430 800 437 760 432 720 440 690 436 640 420 600 416 560 424 520 418 480 426 440 418 400 410 360 414 320 408 280 418 240 412 200 420 160 415 120 422 80 418 40 426 0 420Z"/>
  </svg>

  <header class="brand">
    <svg width="370" height="114" viewBox="0 0 370 114" aria-hidden="true" style="position:absolute;inset:0">
      <path d="M0 0H370V114H38Q22 114 18 100Z" fill="#0d0d0d"/>
    </svg>
    <div class="brand-name">IRONPULSE</div>
    <div class="brand-tag">PERSONAL GROUP TRAINING</div>
  </header>

  <h1 class="title">Coral<br>Blitz<br>Challenge</h1>

  <section class="food-groups">
    <article class="group protein">
      <h2 class="group-tab">PROTEIN</h2>
      <ul>
        <li>4-6 oz chicken breast</li>
        <li>4-6oz turkey breast</li>
        <li>4-6 oz filet mignon</li>
        <li>4-6 oz flank steak</li>
        <li>4-6 oz salmon</li>
        <li>4-6 oz tuna</li>
        <li>4-6 oz cod</li>
        <li>4-6 oz cottage cheese</li>
        <li>4-6 oz greek yogurt</li>
        <li>4-6 oz tofu</li>
        <li>3 -5 egg whites + 1 whole egg</li>
      </ul>
    </article>
    <article class="group fats">
      <h2 class="group-tab">FATS</h2>
      <ul>
        <li>¼ - ½ avocado</li>
        <li>1 tbs olive oil</li>
        <li>1 small handful almonds, walnuts, cashews</li>
      </ul>
    </article>
    <article class="group carbs">
      <h2 class="group-tab">CARBS</h2>
      <ul>
        <li>3 – 4oz sweet potato</li>
        <li>¼ - ½ cup white rice</li>
        <li>¼ - ½ cup quinoa</li>
        <li>¼ - ½ cup oatmeal</li>
        <li>¾ cup blueberries</li>
        <li>¾ cup strawberries</li>
        <li>¾ cup raspberries</li>
        <li>1 med. apple</li>
        <li>1 small orange</li>
        <li>1 small grapefruit</li>
      </ul>
    </article>
    <article class="group veg">
      <h2 class="group-tab">VEGETABLES</h2>
      <ul>
        <li>1 scoop powdered greens</li>
        <li>1 cup sautéed spinach</li>
        <li>1 cup sautéed kale, broccoli</li>
        <li>1 cup sautéed bell pepper</li>
        <li>1 cup sautéed carrots</li>
        <li>1 cup sautéed zucchini</li>
      </ul>
    </article>
  </section>

  <p class="portion-note">NOTE: &lt; 150 LBS STICK TO SMALLER PORTIONS | &gt; 150 LBS STICK TO LARGER PORTIONS.</p>

  <section class="meal-flow">
    <div class="meal" style="left:53px">
      <svg width="152" height="152" viewBox="0 0 152 152">
        <g fill="none" stroke-width="34">
          <circle cx="76" cy="76" r="59" stroke="var(--veg)" stroke-dasharray="119.6 251.1" transform="rotate(30 76 76)"/>
          <circle cx="76" cy="76" r="59" stroke="var(--carbs)" stroke-dasharray="145.3 225.4" transform="rotate(150 76 76)"/>
          <circle cx="76" cy="76" r="59" stroke="var(--protein)" stroke-dasharray="93.8 276.9" transform="rotate(295 76 76)"/>
        </g>
        <g font-family="Oswald, sans-serif" font-size="22" font-weight="500" fill="#0d0d0d" text-anchor="middle">
          <text x="23" y="60">1</text><text x="129" y="60">1</text><text x="76" y="146">1</text>
          <text x="76" y="84" fill="#fff" font-size="21">BREAKFAST</text>
        </g>
      </svg>
    </div>
    <div class="snack" style="left:227px">
      <svg class="snack-arrow" width="100" height="42" viewBox="0 0 100 42"><path d="M0 10H72V0L100 21 72 42V32H0Z" fill="var(--snack)"/><text x="38" y="26" text-anchor="middle" font-family="Archivo Black, sans-serif" font-size="13" fill="#0d0d0d">SNACK</text></svg>
      <p class="snack-note">1/2 PORTION<br>OF PROTEIN</p>
    </div>
    <div class="meal" style="left:364px">
      <svg width="152" height="152" viewBox="0 0 152 152">
        <g fill="none" stroke-width="34">
          <circle cx="76" cy="76" r="59" stroke="var(--veg)" stroke-dasharray="119.6 251.1" transform="rotate(30 76 76)"/>
          <circle cx="76" cy="76" r="59" stroke="var(--carbs)" stroke-dasharray="145.3 225.4" transform="rotate(150 76 76)"/>
          <circle cx="76" cy="76" r="59" stroke="var(--protein)" stroke-dasharray="93.8 276.9" transform="rotate(295 76 76)"/>
        </g>
        <g font-family="Oswald, sans-serif" font-size="22" font-weight="500" fill="#0d0d0d" text-anchor="middle">
          <text x="23" y="60">1</text><text x="129" y="60">1</text><text x="76" y="146">1</text>
          <text x="76" y="84" fill="#fff" font-size="21">LUNCH</text>
        </g>
      </svg>
    </div>
    <div class="snack" style="left:545px">
      <svg class="snack-arrow" width="100" height="42" viewBox="0 0 100 42"><path d="M0 10H72V0L100 21 72 42V32H0Z" fill="var(--snack)"/><text x="38" y="26" text-anchor="middle" font-family="Archivo Black, sans-serif" font-size="13" fill="#0d0d0d">SNACK</text></svg>
      <p class="snack-note">1/2 PORTION<br>OF PROTEIN</p>
    </div>
    <div class="meal" style="left:682px">
      <svg width="152" height="152" viewBox="0 0 152 152">
        <g fill="none" stroke-width="34">
          <circle cx="76" cy="76" r="59" stroke="var(--veg)" stroke-dasharray="119.6 251.1" transform="rotate(30 76 76)"/>
          <circle cx="76" cy="76" r="59" stroke="var(--fats)" stroke-dasharray="145.3 225.4" transform="rotate(150 76 76)"/>
          <circle cx="76" cy="76" r="59" stroke="var(--protein)" stroke-dasharray="93.8 276.9" transform="rotate(295 76 76)"/>
        </g>
        <g font-family="Oswald, sans-serif" font-size="22" font-weight="500" fill="#0d0d0d" text-anchor="middle">
          <text x="23" y="60">1</text><text x="129" y="60">1</text><text x="76" y="146">1</text>
          <text x="76" y="84" fill="#fff" font-size="21">DINNER</text>
        </g>
      </svg>
    </div>
  </section>

  <h2 class="fuel-title">FUEL YOUR CORAL BLITZ!</h2>
  <p class="fuel-intro">THIS PLAN ISN'T ABOUT STARVING YOURSELF - IT'S ABOUT SCULPTING A LEAN, TONED PHYSIQUE BY SHREDDING FAT WHILE PRESERVING MUSCLE. HERE'S HOW TO MAXIMIZE YOUR RESULTS:</p>

  <section class="tips">
    <div class="tip" style="left:39px;width:125px"><h3>Eat like a<br>champion</h3><p>Stick to this list as close as possible for maximum results, 7 Days A Week.</p></div>
    <span class="tip-rule" style="left:170px"></span>
    <div class="tip" style="left:198px;width:150px"><h3>Burn more than<br>you consume</h3><p>This is the golden rule! You need to burn more calories than you consume to create a deficit and force your body to tap into fat stores for energy.</p></div>
    <span class="tip-rule" style="left:355px"></span>
    <div class="tip" style="left:381px;width:150px"><h3>Prioritize<br>protein</h3><p>Protein helps build and maintain muscle mass, which is crucial for boosting metabolism and burning more calories at rest.</p></div>
    <span class="tip-rule" style="left:540px"></span>
    <div class="tip" style="left:554px;width:160px"><h3>Maximize<br>sleep</h3><p>When sleep-deprived, your body produces more ghrelin (hunger hormone) and less leptin (satiety hormone). Aim for 7-8 hours of quality sleep nightly.</p></div>
    <span class="tip-rule" style="left:725px"></span>
    <div class="tip" style="left:742px;width:165px"><h3>Consistency<br>is king/queen</h3><p>Don't expect overnight results. Stick to your plan, track your progress, and celebrate small victories. Remember, slow and steady wins the shred race!</p></div>
  </section>
</main>
</body>
</html>
```